Touchscreen Desktop App for Solar Industry

We need an app design for a custom program we are creating for a client of ours. This app will be used on an exhibit floor and will have the following features: Data Capturing, User Survey Questions, and an electronic literature component (product thumbnails that user taps and then has a PDF sent to them). The app should have a consistent background, universal navigation elements, and support the corporate branding guidelines. The style should be modern (no heavy bezel or embossing), user-friendly, with an overall clean, uncluttered look.

Target Market(s)

Solar power buyers and sellers

Industry/Entity Type

Solar Energy

Font styles to use
Sans Serif

Requirements
Must have
• Good placement of logo. Consistent placement of navigation, preferably at the bottom of the screen. Three sections: Data Capturing Screen (first name, last name, company, email, phone.); Survey Screen to include a single question with multiple choice answers (radio buttons or check boxes); Electronic literature with thumbnails of items, a "Check-Out" button, a screen listing items to be ordered and confirming order.
Should not have
• No sunflowers, grass or Sun w/its rays. That imagery has been done to death in the solar industry. The design should reflect the KRV brand, not be focused on a solar industry.

```html
<!DOCTYPE html>
<html lang="en">
<head>
<meta charset="utf-8">
<title>KRV Exhibit Kiosk – Screens</title>
<link rel="stylesheet" href="https://fonts.googleapis.com/css2?family=Share+Tech+Mono&display=swap">
<style>
  :root{
    --page:#ffffff;
    --screen-top:#f4f4fc;
    --screen-bottom:#e6e6f6;
    --brand:#3a64b8;
    --brand-deep:#1f3f8f;
    --band-light:#dfe6f8;
    --band-mid:#7f9ddc;
    --field-border:#6f8fd2;
    --field:#ffffff;
    --ink:#27305a;
    --logo:#0d1a5c;
    --nav-text:#e8eeff;
  }
  *{box-sizing:border-box;margin:0;padding:0}
  html,body{width:855px;height:1200px;overflow:hidden;background:var(--page)}
  body{position:relative;font-family:"Share Tech Mono",monospace;color:var(--ink)}

  .screen{position:absolute;left:162px;width:530px;height:300px;
    background:linear-gradient(180deg,var(--screen-top),var(--screen-bottom));
    overflow:hidden;box-shadow:0 0 0 1px #d6d8ee}
  .screen--info{top:85px}
  .screen--survey{top:442px}
  .screen--docs{top:806px}

  .header-band{position:absolute;left:150px;top:0;width:380px;height:60px;
    background:linear-gradient(90deg,rgba(223,230,248,0) 0%,var(--band-light) 30%,var(--band-mid) 70%,var(--brand) 100%)}

  .brand{position:absolute;left:14px;top:14px}
  .brand__name{font-size:34px;line-height:30px;color:var(--logo);letter-spacing:1px}
  .brand__tag{font-size:7px;letter-spacing:.5px;color:var(--logo);margin-top:2px}

  .screen__title{position:absolute;left:330px;top:40px;font-size:14px;line-height:16px;letter-spacing:4px;color:#fff;white-space:nowrap}

  .label{position:absolute;right:336px;font-size:14px;letter-spacing:4px;line-height:17px;text-align:right;white-space:nowrap}
  .field{position:absolute;left:208px;width:228px;height:17px;background:var(--field);border:1px solid var(--field-border);border-radius:2px}
  .field--short{width:206px}
  .radio{position:absolute;left:420px;width:13px;height:13px;border-radius:50%;background:#fff;border:2px solid var(--brand)}
  .radio::after{content:"";position:absolute;left:2px;top:2px;width:5px;height:5px;border-radius:50%;background:var(--brand)}

  .btn{position:absolute;height:17px;width:91px;background:linear-gradient(180deg,#5a82d2,var(--brand));
    color:#fff;font-size:10px;letter-spacing:4px;text-align:center;line-height:17px}
  .btn--submit{left:217px;top:248px}
  .btn--reset{left:342px;top:248px}
  .btn--send{left:407px;top:237px}

  .folder{position:absolute;width:63px;height:46px}
  .folder__pick{position:absolute;width:12px;height:12px;border-radius:50%;background:#fff;border:2px solid var(--brand)}
  .folder__pick::after{content:"";position:absolute;left:2px;top:2px;width:4px;height:4px;border-radius:50%;background:var(--brand)}

  .nav{position:absolute;left:0;bottom:0;width:100%;height:22px;background:linear-gradient(180deg,#4d74c6,var(--brand-deep))}
  .nav__item{position:absolute;top:4px;font-size:11px;line-height:14px;letter-spacing:3px;color:var(--nav-text);white-space:nowrap}
  .nav__item:nth-child(1){left:98px}
  .nav__item:nth-child(2){left:220px}
  .nav__item:nth-child(3){left:338px}
</style>
</head>
<body>

<section class="screen screen--info">
  <div class="header-band" role="img" aria-label="Decorative blue wave band across the header"></div>
  <div class="brand"><div class="brand__name">KRV</div><div class="brand__tag">KRV ENERGY SOLUTIONS</div></div>
  <div class="screen__title">YOUR INFO</div>

  <div class="label" style="top:103px">first name:</div><div class="field" style="top:103px"></div>
  <div class="label" style="top:128px">last name:</div><div class="field" style="top:128px"></div>
  <div class="label" style="top:154px">company:</div><div class="field" style="top:154px"></div>
  <div class="label" style="top:180px">email:</div><div class="field" style="top:180px"></div>
  <div class="label" style="top:206px">phone:</div><div class="field" style="top:206px"></div>

  <div class="btn btn--submit">submit</div>
  <div class="btn btn--reset">reset</div>

  <nav class="nav"><span class="nav__item">YOUR INFO</span><span class="nav__item">QUESTIONS</span><span class="nav__item">DOCUMENTS</span></nav>
</section>

<section class="screen screen--survey">
  <div class="header-band" role="img" aria-label="Decorative blue wave band across the header"></div>
  <div class="brand"><div class="brand__name">KRV</div><div class="brand__tag">KRV ENERGY SOLUTIONS</div></div>
  <div class="screen__title">QUESTIONS</div>

  <div class="label" style="top:94px">what is ?:</div><div class="field" style="top:94px"></div>
  <div class="field field--short" style="top:120px"></div><div class="radio" style="top:122px"></div>
  <div class="field field--short" style="top:146px"></div><div class="radio" style="top:148px"></div>
  <div class="field field--short" style="top:172px"></div><div class="radio" style="top:174px"></div>
  <div class="label" style="top:213px">answer:</div><div class="field" style="top:213px"></div>

  <div class="btn btn--submit">submit</div>
  <div class="btn btn--reset">reset</div>

  <nav class="nav"><span class="nav__item">YOUR INFO</span><span class="nav__item">QUESTIONS</span><span class="nav__item">DOCUMENTS</span></nav>
</section>

<section class="screen screen--docs">
  <div class="header-band" role="img" aria-label="Decorative blue wave band across the header"></div>
  <div class="brand"><div class="brand__name">KRV</div><div class="brand__tag">KRV ENERGY SOLUTIONS</div></div>

  <svg width="0" height="0" aria-hidden="true" style="position:absolute">
    <symbol id="folder" viewBox="0 0 63 46">
      <path d="M1 6 H22 L27 1 H62 V45 H1Z" fill="#fff" stroke="#6f8fd2" stroke-width="1.5"/>
      <path d="M1 10 H62" stroke="#c3d0ef" stroke-width="1"/>
    </symbol>
  </svg>

  <svg class="folder" style="left:57px;top:80px"><use href="#folder"/></svg><span class="folder__pick" style="left:124px;top:112px"></span>
  <svg class="folder" style="left:171px;top:80px"><use href="#folder"/></svg><span class="folder__pick" style="left:238px;top:112px"></span>
  <svg class="folder" style="left:285px;top:80px"><use href="#folder"/></svg><span class="folder__pick" style="left:352px;top:112px"></span>
  <svg class="folder" style="left:399px;top:80px"><use href="#folder"/></svg><span class="folder__pick" style="left:466px;top:112px"></span>

  <svg class="folder" style="left:57px;top:155px"><use href="#folder"/></svg><span class="folder__pick" style="left:124px;top:187px"></span>
  <svg class="folder" style="left:171px;top:155px"><use href="#folder"/></svg><span class="folder__pick" style="left:238px;top:187px"></span>
  <svg class="folder" style="left:285px;top:155px"><use href="#folder"/></svg><span class="folder__pick" style="left:352px;top:187px"></span>
  <svg class="folder" style="left:399px;top:155px"><use href="#folder"/></svg><span class="folder__pick" style="left:466px;top:187px"></span>

  <div class="btn btn--send">send</div>

  <nav class="nav"><span class="nav__item">YOUR INFO</span><span class="nav__item">QUESTIONS</span><span class="nav__item">DOCUMENTS</span></nav>
</section>

</body>
</html>
```